Freelancers in the field of IT security and IT service need a business card design

I need a business card design for my company. I am a freelancer and active in the area of IT security, IT support% 26 # 252; tung, consulting. I am not yet color-coded, but it should be a modern color that can also be used for a later website. The design should be innovation. Exude dynamism and reliability

Target Market(s)

IT security, IT solutions

Contact Information for Business Card

Firma: brandel-advisory, Inhaber: Jonas Wirtel
Adresse: Lindenhang 4, D-73218 Moorfelden
Telefon: +49 (0) 7354 608193
E-Mail Jonas.Wirtel@brandel-advisory.example

```html
<!DOCTYPE html>
<html lang="de">
<head>
<meta charset="utf-8">
<title>Brandel Advisory – Visitenkarte</title>
<link rel="stylesheet" href="https://fonts.googleapis.com/css2?family=Montserrat:wght@600;700&family=Open+Sans:wght@400&display=swap">
<style>
  :root {
    --stage: #2a2a2a;
    --card: #1e1e1f;
    --orange: #f7a01b;
    --grey: #8a8a8a;
    --text-light: #bfbfbf;
    --divider: #555555;
  }
  * { box-sizing: border-box; margin: 0; padding: 0; }
  html, body { width: 1200px; height: 1108px; overflow: hidden; background: var(--stage); }
  .stage {
    width: 1200px; height: 1108px;
    display: flex; flex-direction: column; align-items: center; justify-content: center; gap: 48px;
  }
  .card {
    position: relative; width: 840px; height: 480px;
    background: var(--card); border-radius: 26px; overflow: hidden;
    box-shadow: 0 14px 34px rgba(0,0,0,.45);
  }
  .card-front .edge-bands { position: absolute; left: 0; right: 0; bottom: 0; height: 30px; }
  .edge-bands .band-grey { position: absolute; left: 0; right: 0; top: 0; height: 12px; background: var(--grey); }
  .edge-bands .band-orange { position: absolute; left: 0; right: 0; bottom: 0; height: 18px; background: var(--orange); }
  .brand { position: absolute; display: flex; align-items: center; gap: 18px; }
  .card-front .brand { left: 56px; top: 190px; }
  .brand-dot { width: 58px; height: 58px; border-radius: 50%; background: var(--grey); flex: none; }
  .brand-name {
    font-family: "Montserrat", sans-serif; font-weight: 700; color: var(--orange);
    font-size: 38px; line-height: 1.05; letter-spacing: 1px; text-transform: uppercase;
  }
  .contact {
    position: absolute; left: 410px; top: 118px;
    font-family: "Open Sans", sans-serif; color: var(--text-light);
  }
  .contact-name {
    font-family: "Montserrat", sans-serif; font-weight: 700; color: var(--orange);
    font-size: 30px; text-transform: uppercase; line-height: 1.1;
  }
  .contact-role { font-size: 18px; margin-top: 4px; }
  .contact-group {
    border-top: 1px solid var(--divider); margin-top: 16px; padding-top: 14px;
    font-size: 17px; line-height: 1.5; width: 380px; white-space: nowrap;
  }
  .contact-line { display: flex; align-items: center; gap: 10px; }
  .contact-line svg { flex: none; }
  .card-back .brand { left: 50%; top: 50%; transform: translate(-50%, -50%); }
  .card-back .brand-block { display: flex; flex-direction: column; gap: 10px; }
  .tagline { font-family: "Open Sans", sans-serif; color: var(--orange); font-size: 20px; letter-spacing: 1px; text-transform: uppercase; }
  .card-back .brand-name { font-size: 52px; }
  .card-back .brand-dot { width: 72px; height: 72px; }
</style>
</head>
<body>
<main class="stage">
  <section class="card card-front" aria-label="Vorderseite">
    <div class="brand">
      <span class="brand-dot"></span>
      <span class="brand-name">Brandel<br>Advisory</span>
    </div>
    <div class="contact">
      <p class="contact-name">Jonas Wirtel</p>
      <p class="contact-role">Geschäftsführer</p>
      <div class="contact-group">
        <p>Lindenhang 4</p>
        <p>D-73218 Moorfelden</p>
      </div>
      <div class="contact-group">
        <p class="contact-line">
          <svg width="16" height="16" viewBox="0 0 16 16"><rect x="0.5" y="0.5" width="15" height="15" rx="2" fill="none" stroke="var(--orange)"/><path d="M5 3.5l2 2-1 1.2c.6 1.4 1.6 2.4 3 3l1.2-1 2 2-1.3 1.8C7.5 12 4 8.5 3.5 5.2z" fill="var(--orange)"/></svg>
          +49 (0) 7354 608193
        </p>
        <p class="contact-line">
          <svg width="16" height="16" viewBox="0 0 16 16"><rect x="0" y="2" width="16" height="12" fill="var(--orange)"/><path d="M0 2l8 6 8-6" fill="none" stroke="var(--card)" stroke-width="1.4"/></svg>
          Jonas.Wirtel@brandel-advisory.example
        </p>
      </div>
    </div>
    <div class="edge-bands"><span class="band-grey"></span><span class="band-orange"></span></div>
  </section>

  <section class="card card-back" aria-label="Rückseite">
    <div class="brand">
      <span class="brand-dot"></span>
      <div class="brand-block">
        <span class="brand-name">Brandel<br>Advisory</span>
        <span class="tagline">IT-Service &amp; Sicherheit</span>
      </div>
    </div>
  </section>
</main>
</body>
</html>
```